Valbrook Data Works

Our company is about IT hardwares and IT solutions. IT hardware such as PC, RAMS, storage and servers. IT solutions such as project management, BA. We are also selling new technology too.

Target Market(s)

Consumer, Small to Medium Business, Corporate

Requirements
Must have
• The business card must have the following:
• Name:
• Title:
• Contact Number:
• Email address:
• Website:
• Color: Must match the logo color upgrade

```html
<!DOCTYPE html>
<html lang="en">
<head>
<meta charset="UTF-8">
<title>Valbrook Data Works — Business Card</title>
<link rel="stylesheet" href="https://fonts.googleapis.com/css2?family=Lato:wght@300;400&family=Raleway:wght@400;700&family=Roboto:wght@400&display=swap">
<style>
  :root {
    --backdrop: #4a4d52;
    --card: #070707;
    --gold: #f6ad2b;
    --gold-deep: #e58a1f;
    --gold-muted: #7a6226;
    --olive: #4d4320;
    --white: #ffffff;
  }
  * { margin: 0; padding: 0; box-sizing: border-box; }
  html, body { width: 1200px; height: 1200px; overflow: hidden; }
  body {
    background: var(--backdrop);
    font-family: "Raleway", sans-serif;
    position: relative;
  }
  .card {
    position: absolute;
    left: 150px;
    width: 900px;
    height: 514px;
    background: var(--card);
    border-radius: 36px;
    overflow: hidden;
  }
  .card--front { top: 70px; }
  .card--back { top: 616px; }

  /* front */
  .front-pattern {
    position: absolute;
    left: 0; top: 0;
    width: 900px; height: 290px;
    background: linear-gradient(200deg, var(--gold) 0%, var(--gold-muted) 35%, var(--olive) 60%, #1a1608 85%);
    clip-path: polygon(0 0, 100% 0, 96% 8%, 80% 22%, 62% 45%, 50% 70%, 40% 100%, 28% 82%, 14% 70%, 0 62%);
  }
  .front-brand {
    position: absolute;
    left: 0; right: 0; top: 300px;
    text-align: center;
  }
  .brand-mark {
    display: inline-flex;
    align-items: center;
    gap: 14px;
  }
  .brand-dot {
    width: 30px; height: 30px;
    border-radius: 50%;
    background: var(--gold-deep);
  }
  .brand-name {
    font-family: "Raleway", sans-serif;
    font-weight: 700;
    font-size: 40px;
    color: var(--white);
    letter-spacing: 1px;
  }
  .tagline-row {
    display: flex;
    align-items: center;
    gap: 22px;
    margin-top: 34px;
    padding: 0 40px;
  }
  .tagline-rule {
    flex: 1;
    height: 1px;
    background: var(--gold-deep);
  }
  .tagline {
    font-family: "Lato", sans-serif;
    font-weight: 300;
    font-size: 30px;
    color: var(--gold-deep);
    white-space: nowrap;
  }

  /* back */
  .back-pattern {
    position: absolute;
    left: 0; top: 0;
    width: 560px; height: 514px;
    background: linear-gradient(60deg, var(--gold-deep) 0%, var(--gold) 30%, #b58b2a 55%, var(--olive) 78%, #1c180a 100%);
    clip-path: polygon(0 12%, 12% 6%, 30% 0, 44% 3%, 58% 14%, 70% 30%, 84% 48%, 100% 62%, 92% 80%, 80% 100%, 0 100%);
  }
  .back-info {
    position: absolute;
    right: 60px; top: 50px;
    width: 380px;
    text-align: right;
  }
  .back-info .brand-name { font-size: 28px; }
  .back-info .brand-dot { width: 22px; height: 22px; }
  .person-name {
    margin-top: 30px;
    font-weight: 400;
    font-size: 44px;
    color: var(--white);
  }
  .person-title {
    font-family: "Lato", sans-serif;
    font-weight: 300;
    font-size: 28px;
    color: var(--gold-deep);
    margin-top: 2px;
  }
  .contacts {
    list-style: none;
    margin-top: 38px;
  }
  .contact-group {
    display: flex;
    justify-content: flex-end;
    align-items: flex-start;
    gap: 22px;
    margin-bottom: 14px;
  }
  .contact-lines {
    font-family: "Roboto", sans-serif;
    font-size: 22px;
    line-height: 30px;
    color: var(--white);
  }
  .contact-icon { width: 30px; height: 30px; flex: none; margin-top: 2px; }
</style>
</head>
<body>

<section class="card card--front">
  <div class="front-pattern" role="img" aria-label="Cascade of gold, olive and black geometric triangles across the top edge"></div>
  <div class="front-brand">
    <div class="brand-mark">
      <span class="brand-dot"></span>
      <span class="brand-name">Valbrook Data Works</span>
    </div>
    <div class="tagline-row">
      <span class="tagline-rule"></span>
      <span class="tagline">IT hardwares &amp; IT solutions</span>
      <span class="tagline-rule"></span>
    </div>
  </div>
</section>

<section class="card card--back">
  <div class="back-pattern" role="img" aria-label="Gold and olive triangle mosaic fading to black from the lower left"></div>
  <div class="back-info">
    <div class="brand-mark">
      <span class="brand-dot"></span>
      <span class="brand-name">Valbrook Data Works</span>
    </div>
    <h1 class="person-name">Marcus Ellery</h1>
    <p class="person-title">Managing Director</p>
    <ul class="contacts">
      <li class="contact-group">
        <div class="contact-lines">011 480 7315<br>012 366 9041</div>
        <svg class="contact-icon" viewBox="0 0 24 24" aria-hidden="true">
          <path fill="var(--gold-deep)" d="M6.6 10.8a15.1 15.1 0 0 0 6.6 6.6l2.2-2.2a1 1 0 0 1 1-.25 11.4 11.4 0 0 0 3.6.57 1 1 0 0 1 1 1V20a1 1 0 0 1-1 1A17 17 0 0 1 3 4a1 1 0 0 1 1-1h3.5a1 1 0 0 1 1 1c0 1.25.2 2.45.57 3.57a1 1 0 0 1-.25 1z"/>
        </svg>
      </li>
      <li class="contact-group">
        <div class="contact-lines">info@valbrookdata.com<br>www.valbrookdata.com</div>
        <svg class="contact-icon" viewBox="0 0 24 24" aria-hidden="true">
          <g fill="none" stroke="var(--gold-deep)" stroke-width="1.8">
            <circle cx="12" cy="12" r="9.5"/>
            <ellipse cx="12" cy="12" rx="4.2" ry="9.5"/>
            <line x1="2.5" y1="12" x2="21.5" y2="12"/>
            <path d="M4.5 7h15M4.5 17h15"/>
          </g>
        </svg>
      </li>
      <li class="contact-group">
        <div class="contact-lines">2480 Harlow Avenue<br>Fairmont, Ca 30917</div>
        <svg class="contact-icon" viewBox="0 0 24 24" aria-hidden="true">
          <path fill="var(--gold-deep)" d="M12 2a7 7 0 0 0-7 7c0 5.2 7 13 7 13s7-7.8 7-13a7 7 0 0 0-7-7zm0 9.5A2.5 2.5 0 1 1 12 6.5a2.5 2.5 0 0 1 0 5z"/>
        </svg>
      </li>
    </ul>
  </div>
</section>

</body>
</html>
```